Clean book cover design for book about writing a book

Book title: The Crossing
Subtitle: 9 Paths to Crafting a Volume that Counts
Name: Marisol T. Brenwick, The Quill Nursery

This is a book which teaches 10 steps to writing a self-help book. I'm looking for a very clean impactful cover either with no image or just a small simple image of a book, typewriter, laptop, cabin or something very simple. I am attaching the manuscript here if reading it would help you with the cover. The theme of the book is that you can write with joy and ease and your book can just flow out of you if you learn how to clear the blocks between you and your book already written. Sort of a new agey stance on book writing.

The book should generally match the branding on my website. Www.TheQuillNursery.example.

I have photos of myself attached which I'd like used for the back cover with an "about the author section of maybe 50 words.

The project is for the full back cover and spine as well as the front cover (see print Forge template attached) but to win the contest you can just design the front cover and then I'll give the winner the template for the full design with the back cover copy. Or you can design the full cover using the template and you can use Loren ipsum text if you need to.

My clients are very upmarket and the themes of my business revolve around nuturing and incubating ideas and authors. Very feminine creation energy.

For colors see The Crossing Press (CB) wax seals and the background fades. I don't want my logo on the cover but I am attaching it here so you get a feel for the branding. The logo is in the LOBSTER font and you can see how we do the grey with the rainbow shadow.

Here are some covers I like:

http://www.shopvale.example/Pen-Tome-Quick-Stage---Stage/dp/055817342Q
http://www.shopvale.example/Plotting-Your-Tale-Chart-Triumph/dp/0841739265
http://www.shopvale.example/Be-Scribe-Seeking-Voice-Guide-ebook/dp/K22R9WQ3L1
http://www.shopvale.example/Strays-Tale-Triumph-Rupert-Vanhollow/dp/0552048871
Updates

I have revised my brief to include some picture and images that will help you create the cover. I have also included some of my favorite covers to give you more of a sense of what I'm going for. And I have included the manuscript in case it would help you to skim through it in order to get a sense of the reader and the book. I think if you look at my revised brief it will make it easier to create a submission. Thanks!

Target Market(s)

Women 40-60 who run small businesses as life coaches or other healing jobs (therapy, reiki, light work) they have a spiritual/new age bent.

Industry/Entity Type

Business

Font styles to use
Serif
Other font styles liked:
• Lobster (not required... just a suggestion since it's my logo font)

Requirements
Must have
• Name and title easy to read in 1" x 1" thumb nail
Nice to have
• Fantastic type face treatment.

Match the look and feel of my website.
Should not have
• Busy images. With one simple image or just designed with colors and typeface treatment

```html
<!DOCTYPE html>
<html lang="en">
<head>
<meta charset="utf-8">
<title>The Crossing — Book Cover</title>
<link rel="stylesheet" href="https://fonts.googleapis.com/css2?family=Oswald:wght@300;400&family=Playfair+Display:wght@700&family=Titan+One&display=swap">
<style>
  :root {
    --stage: #161616;
    --wood-dark: #1e140c;
    --wood-mid: #4a3524;
    --wood-warm: #6b4e33;
    --title-cream: #efe6d6;
    --title-gold: #b8893e;
    --sub-white: #ffffff;
    --sub-shadow: #1a120b;
    --paper: #f1ede4;
    --paper-edge: #d9d3c6;
    --seal: #3aa7b8;
    --byline: #f4efe6;
  }
  * { margin: 0; padding: 0; box-sizing: border-box; }
  html, body {
    width: 1200px; height: 1116px; overflow: hidden;
    background: var(--stage);
  }
  .cover {
    position: absolute; left: 184px; top: 20px;
    width: 832px; height: 1076px; overflow: hidden;
  }
  .cover-backdrop {
    position: absolute; inset: 0;
    background:
      radial-gradient(ellipse at 35% 80%, rgba(120,95,70,0.45), transparent 55%),
      linear-gradient(100deg, var(--wood-dark) 0%, var(--wood-mid) 30%, var(--wood-warm) 50%, var(--wood-mid) 70%, var(--wood-dark) 100%);
  }
  .paper-art { position: absolute; inset: 0; }
  .title-article {
    position: absolute; left: 60px; top: 118px;
    width: 100px; height: 40px;
    transform-origin: 0 0; transform: rotate(90deg) translate(0, -40px);
    font-family: "Playfair Display", serif; font-weight: 700;
    font-size: 38px; line-height: 40px; letter-spacing: 2px;
    color: var(--title-gold);
  }
  .title-main {
    position: absolute; left: 134px; top: 84px;
    font-family: "Oswald", sans-serif; font-weight: 300;
    font-size: 160px; line-height: 160px; letter-spacing: 4px;
    color: var(--title-cream);
  }
  .subtitle {
    position: absolute; left: 52px; top: 388px;
    font-family: "Titan One", sans-serif;
    color: var(--sub-white);
    text-shadow: 3px 4px 0 var(--sub-shadow), 5px 7px 10px rgba(0,0,0,0.6);
    text-transform: uppercase;
  }
  .subtitle span { display: block; }
  .sub-number { font-size: 92px; line-height: 96px; }
  .sub-small { font-size: 52px; line-height: 56px; }
  .sub-line1 { display: flex; align-items: baseline; gap: 12px; }
  .sub-line2 { margin-top: 8px; }
  .sub-big { font-size: 108px; line-height: 120px; margin-top: 12px; }
  .sub-line4 { margin-top: 4px; }
  .imprint {
    position: absolute; left: 748px; top: 878px;
    display: flex; align-items: center; gap: 6px;
    font-family: "Oswald", sans-serif; font-weight: 400;
    font-size: 20px; color: var(--seal);
  }
  .imprint-dot { width: 14px; height: 14px; border-radius: 50%; background: var(--seal); }
  .byline {
    position: absolute; left: 576px; top: 976px;
    font-family: "Oswald", sans-serif; font-weight: 300;
    font-size: 19px; line-height: 34px; letter-spacing: 0.5px;
    color: var(--byline); text-transform: uppercase;
  }
</style>
</head>
<body>
  <main class="cover">
    <div class="cover-backdrop" role="img" aria-label="Photograph of weathered dark wood with a faded vintage typewriter keyboard"></div>
    <svg class="paper-art" width="832" height="1076" viewBox="0 0 832 1076" role="img" aria-label="Photograph of a sheet of cream paper with a fountain pen resting on it">
      <polygon points="832,247 465,441 736,946 832,893" fill="var(--paper)" stroke="var(--paper-edge)" stroke-width="2"/>
    </svg>

    <h1 class="title">
      <span class="title-article">THE</span>
      <span class="title-main">CROSSING</span>
    </h1>

    <h2 class="subtitle">
      <span class="sub-line1"><span class="sub-number">9</span><span class="sub-small">Paths</span></span>
      <span class="sub-small sub-line2">To Crafting</span>
      <span class="sub-big">A Volume</span>
      <span class="sub-small sub-line4">That Counts</span>
    </h2>

    <div class="imprint"><span class="imprint-dot"></span>CB</div>

    <p class="byline">Marisol T. Brenwick,<br>The Quill Nursery</p>
  </main>
</body>
</html>
```